Design for Employee Baseball Cards

Looking to design baseball cards for my employees. Trying to replicate famous baseball card design with swapping in an employee and listing there stats and fun facts. These cards will be inserted into boxes so customers can receive with their orders. Cards allow customers to put a face to the name they've always corresponded with, which makes their experience personable and more memorable.

Looking for a front and back design template. We are open to the design, but would like it to resemble a baseball/playing card.
Size: 2.5" x 3.5" vertical
Here is our website which can be referenced for color pallet and tone.
https://www.crateswithmarlow.com/

Attached is an example of a vintage baseball. Can we see some versions like this?

Front
- Person's name
- Title/Department
- Crates With Marlow logo
- Person's photo - this will be an action shot like a baseball card

Back
I'm open to the design and content of the back. We want it to resemble a back of a baseball card as best as possible. Normally, baseball cards will have stats by year. Instead, we can have stats and fun facts like the following

Items for Back
- Bio
- Year started at CWM
- Department
- Years of experience
- Specialty
- Secret skill
- What you love about CWM
- Favorite quote
- Fun fact
- Passion outside of CWM
- Person's photo - we can include a smaller headshot

Font styles to use
Sans Serif

Colors
0054AA
0677BA
7BADD7
CADEEF
E8F1F8

Requirements
Must have
• The deliverable must be a template PSD or AI that we can swap in photos and edit text for each person's card.

```html
<!DOCTYPE html>
<html lang="en">
<head>
<meta charset="utf-8">
<title>Employee Trading Card – Front and Back</title>
<link rel="stylesheet" href="https://fonts.googleapis.com/css2?family=Arimo:wght@400;700&family=Roboto+Condensed:wght@400&display=swap">
<style>
  :root {
    --navy: #1d3868;
    --steel: #8ea7c7;
    --sky: #5d9ad3;
    --red: #d7263d;
    --white: #ffffff;
    --ink: #111111;
  }
  * { box-sizing: border-box; margin: 0; padding: 0; }
  html, body { width: 1200px; height: 997px; overflow: hidden; background: var(--white); }
  .stage {
    position: relative; width: 1265px; height: 1051px;
    transform: scale(0.94862); transform-origin: 0 0;
  }
  .card { position: absolute; top: 40px; width: 555px; height: 970px; overflow: hidden; }
  .card--front { left: 48px; }
  .card--back { left: 662px; }
  .card__art { position: absolute; inset: 0; }

  .name { position: absolute; color: var(--white); font-family: "Arimo", Arial, sans-serif; line-height: 1; white-space: nowrap; }
  .name__first { font-size: 48px; font-weight: 400; }
  .name__last { font-size: 48px; font-weight: 700; margin-top: -4px; }
  .name__roles { display: flex; justify-content: space-between; font-size: 17px; margin-top: 4px; }

  .card--front .name { left: 220px; top: 834px; width: 300px; }
  .card--back .name { left: 33px; top: 42px; width: 308px; }

  .brand { position: absolute; display: flex; align-items: center; gap: 10px; font-family: "Arimo", Arial, sans-serif; }
  .brand__mark { width: 34px; height: 34px; flex: none; }
  .brand__name { font-size: 22px; font-weight: 400; line-height: 1.05; white-space: nowrap; }
  .brand__tagline { position: absolute; font-family: "Arimo", Arial, sans-serif; font-size: 7px; white-space: nowrap; }

  .card--front .brand { left: 22px; top: 862px; color: var(--white); }
  .card--front .brand__mark { background: var(--white); }
  .card--front .brand__tagline { left: 66px; top: 915px; color: var(--white); }
  .card--back .brand { left: 68px; top: 216px; color: var(--navy); }
  .card--back .brand__mark { background: var(--navy); width: 40px; height: 40px; }
  .card--back .brand__name { font-size: 25px; }
  .card--back .brand__tagline { left: 120px; top: 268px; color: var(--navy); }

  .stat { position: absolute; font-family: "Roboto Condensed", "Arial Narrow", sans-serif; }
  .stat__label {
    height: 30px; background: var(--red); color: var(--white);
    font-size: 23px; line-height: 30px; white-space: nowrap;
  }
  .stat__value { color: var(--ink); font-size: 23px; margin-top: 8px; white-space: nowrap; }
  .stat--left { left: 0; width: 245px; }
  .stat--left .stat__label { padding-left: 53px; clip-path: polygon(0 0, 100% 0, 88% 100%, 0 100%); }
  .stat--left .stat__value { padding-left: 53px; }
  .stat--right { left: 310px; width: 245px; }
  .stat--right .stat__label { padding-left: 35px; clip-path: polygon(12% 0, 100% 0, 100% 100%, 0 100%); }
  .stat--right .stat__value { padding-left: 33px; }

  .prompt { position: absolute; left: 0; width: 555px; font-family: "Roboto Condensed", "Arial Narrow", sans-serif; }
  .prompt__box {
    position: absolute; left: 62px; top: 4px; width: 432px; height: 95px;
    border: 2px solid var(--steel); border-radius: 8px; background: var(--white);
  }
  .prompt__label {
    position: relative; width: 370px; height: 30px; background: var(--red); color: var(--white);
    font-size: 23px; line-height: 30px; padding-left: 53px; white-space: nowrap;
    clip-path: polygon(0 0, 100% 0, 92% 100%, 0 100%);
  }
  .prompt__answer { position: relative; color: var(--ink); font-size: 23px; padding-left: 84px; margin-top: 10px; white-space: nowrap; }
</style>
</head>
<body>
<div class="stage">

  <section class="card card--front">
    <svg class="card__art" width="555" height="970" viewBox="0 0 555 970">
      <defs>
        <linearGradient id="photoTone" x1="0" y1="0" x2="0" y2="1">
          <stop offset="0" stop-color="#7a5a52"/>
          <stop offset="0.45" stop-color="#3a3f52"/>
          <stop offset="1" stop-color="#1f2a3d"/>
        </linearGradient>
      </defs>
      <rect width="555" height="970" fill="var(--steel)"/>
      <rect x="22" y="35" width="512" height="850" rx="42" fill="var(--sky)" stroke="var(--white)" stroke-width="3"/>
      <g role="img" aria-label="Action photo of the employee in baseball uniform holding a bat">
        <rect x="40" y="53" width="477" height="820" rx="28" fill="url(#photoTone)"/>
      </g>
      <polygon points="0,836 480,752 555,740 555,756 0,852" fill="var(--sky)"/>
      <polygon points="0,850 555,756 555,970 0,970" fill="var(--navy)"/>
      <line x1="187" y1="812" x2="187" y2="960" stroke="var(--steel)" stroke-width="2"/>
    </svg>

    <div class="brand">
      <span class="brand__mark"></span>
      <span class="brand__name">Crates With<br>Marlow</span>
    </div>
    <div class="brand__tagline">Packaging that carries your brand</div>

    <div class="name">
      <div class="name__first">JOHN</div>
      <div class="name__last">DELA ROCHE</div>
      <div class="name__roles"><span>TITLE</span><span>DEPARTMENT</span></div>
    </div>
  </section>

  <section class="card card--back">
    <svg class="card__art" width="555" height="970" viewBox="0 0 555 970">
      <defs>
        <linearGradient id="headshotTone" x1="0" y1="0" x2="0" y2="1">
          <stop offset="0" stop-color="#7a5a52"/>
          <stop offset="0.5" stop-color="#3a3f52"/>
          <stop offset="1" stop-color="#1f2a3d"/>
        </linearGradient>
      </defs>
      <rect width="555" height="970" fill="var(--navy)"/>
      <polygon points="0,232 555,125 555,822 0,968" fill="var(--steel)"/>
      <rect x="42" y="200" width="470" height="738" rx="40" fill="var(--white)"/>
      <g role="img" aria-label="Headshot of the employee in baseball helmet">
        <rect x="383" y="53" width="152" height="203" rx="14" fill="url(#headshotTone)" stroke="var(--steel)" stroke-width="3"/>
      </g>
    </svg>

    <div class="name">
      <div class="name__first">JOHN</div>
      <div class="name__last">DELA ROCHE</div>
      <div class="name__roles"><span>TITLE</span><span>DEPARTMENT</span></div>
    </div>

    <div class="brand">
      <span class="brand__mark"></span>
      <span class="brand__name">Crates With<br>Marlow</span>
    </div>
    <div class="brand__tagline">Packaging that carries your brand</div>

    <div class="stat stat--left" style="top:296px"><div class="stat__label">DATE OF BIRTH</div><div class="stat__value">08 / 15 / 1995</div></div>
    <div class="stat stat--right" style="top:296px"><div class="stat__label">HEIGHT</div><div class="stat__value">6' 2"</div></div>
    <div class="stat stat--left" style="top:368px"><div class="stat__label">BIRTHPLACE</div><div class="stat__value">Los Angeles, California</div></div>
    <div class="stat stat--right" style="top:368px"><div class="stat__label">WEIGHT</div><div class="stat__value">190 Lbs</div></div>
    <div class="stat stat--left" style="top:450px"><div class="stat__label">YEAR STARTED AT</div><div class="stat__value">2022</div></div>
    <div class="stat stat--right" style="top:450px"><div class="stat__label">YEARS OF XP</div><div class="stat__value">8</div></div>
    <div class="stat stat--left" style="top:532px"><div class="stat__label">SPECIALTY</div><div class="stat__value">NONE</div></div>
    <div class="stat stat--right" style="top:532px"><div class="stat__label">SECRET SKILL</div><div class="stat__value">NInja Moves</div></div>

    <div class="prompt" style="top:603px">
      <div class="prompt__box"></div>
      <div class="prompt__label">What you love about CWM</div>
      <div class="prompt__answer">State your answer here</div>
    </div>
    <div class="prompt" style="top:711px">
      <div class="prompt__box"></div>
      <div class="prompt__label">Fun Fact</div>
      <div class="prompt__answer">State your answer here</div>
    </div>
    <div class="prompt" style="top:819px">
      <div class="prompt__box"></div>
      <div class="prompt__label">Passion outside of CWM</div>
      <div class="prompt__answer">State your answer here</div>
    </div>
  </section>

</div>
</body>
</html>
```